Business Card Design

I am a Accounting/Bookkeeping company.  As a sideline, I am also a Notary so I would like that somewhere, either in front or perhaps the backside for the notary business.
I found a standard card I really like but didn't like the "little man" standing on the scale.
I love the colors so I am wondering if you would be able to duplicate this without the man and perhaps money or something appropriate on this side of scale
I also need help on the font.  I tend to like feminine styles but am told they are too hard to read.

Target Market(s)
Small businesses, Individuals
Industry/Entity Type
Business
Contact Information for Business Card
The Tidy Ledgerwright
Balancing your books is our specialty
Marisol (Pebbleton) Varnaccio
Accounting Associate
Certified FiscalTrail CountExpert
Notary Public
Serving Sonoma County                            415-362-9184
marisol.varnaccio@plumpost.example

Requirements
Must have
- I would like a glossy card

```html
<!DOCTYPE html>
<html lang="en">
<head>
<meta charset="utf-8">
<title>The Tidy Ledgerwright — Business Card</title>
<link rel="stylesheet" href="https://fonts.googleapis.com/css2?family=Merriweather:wght@300;400;700&display=swap">
<style>
  :root {
    --page-bg: #ececec;
    --card-blue: #4a62a6;
    --title-blue: #3a569c;
    --band-white: #fbfbfb;
    --ink: #1b1b1b;
    --text-light: #dfe5f3;
    --text-white: #ffffff;
    --art-dark: #1d1d22;
    --art-gold: #c9b23a;
  }
  * { margin: 0; padding: 0; box-sizing: border-box; }
  html, body {
    width: 1200px;
    height: 972px;
    overflow: hidden;
    background: var(--page-bg);
  }
  .canvas {
    position: relative;
    width: 1200px;
    height: 972px;
    display: flex;
    align-items: center;
    justify-content: center;
  }
  .card {
    position: relative;
    width: 900px;
    height: 514px;
    background: var(--card-blue);
    font-family: "Merriweather", Georgia, serif;
    overflow: hidden;
    box-shadow: 0 6px 18px rgba(0,0,0,0.12);
  }
  .card__top-strip {
    position: absolute;
    left: 0; top: 0;
    width: 100%;
    height: 42px;
    background: var(--card-blue);
  }
  .card__title-band {
    position: absolute;
    left: 0; top: 42px;
    width: 100%;
    height: 112px;
    background: var(--band-white);
  }
  .brand {
    position: absolute;
    left: 130px;
    top: 58px;
  }
  .brand__name {
    font-weight: 700;
    font-size: 40px;
    color: var(--title-blue);
    line-height: 1.1;
    white-space: nowrap;
  }
  .brand__tagline {
    font-weight: 400;
    font-size: 23px;
    color: var(--ink);
    margin-top: 4px;
    margin-left: 34px;
    white-space: nowrap;
  }
  .scale-art {
    position: absolute;
    left: 610px;
    top: 170px;
    width: 250px;
    height: 180px;
    border-radius: 6px;
    background: linear-gradient(135deg, rgba(29,29,34,0.85) 0%, rgba(29,29,34,0.6) 65%, rgba(201,178,58,0.85) 100%);
  }
  .contact {
    position: absolute;
    left: 100px;
    top: 222px;
    color: var(--text-light);
  }
  .contact__name {
    font-weight: 700;
    font-size: 24px;
    color: var(--text-white);
    white-space: nowrap;
  }
  .contact__role {
    font-weight: 300;
    font-size: 20px;
    margin-left: 22px;
    margin-top: 6px;
    white-space: nowrap;
  }
  .contact__list {
    list-style: none;
    margin-top: 18px;
    margin-left: 24px;
  }
  .contact__item {
    display: flex;
    align-items: center;
    gap: 10px;
    font-weight: 700;
    font-size: 21px;
    color: var(--text-white);
    margin-bottom: 6px;
    white-space: nowrap;
  }
  .contact__icon {
    width: 22px;
    height: 22px;
    flex: none;
  }
  .notary {
    position: absolute;
    left: 124px;
    top: 448px;
    font-weight: 300;
    font-size: 20px;
    color: var(--text-light);
    white-space: nowrap;
  }
</style>
</head>
<body>
<main class="canvas">
  <article class="card">
    <div class="card__top-strip"></div>
    <div class="card__title-band"></div>

    <header class="brand">
      <h1 class="brand__name">The Tidy Ledgerwright</h1>
      <p class="brand__tagline">Balancing your Books is our Specialty</p>
    </header>

    <div class="scale-art" role="img" aria-label="Illustration of a black balance scale with gold coins resting in one pan"></div>

    <section class="contact">
      <h2 class="contact__name">Marisol (Pebbleton) Varnaccio</h2>
      <p class="contact__role">Accounting Associate</p>
      <p class="contact__role">Certified FiscalTrail CountExpert</p>
      <ul class="contact__list">
        <li class="contact__item">
          <svg class="contact__icon" viewBox="0 0 22 22" aria-hidden="true">
            <circle cx="11" cy="11" r="10" fill="#ffffff"/>
            <path d="M8 6.5c.6-.4 1.2-.2 1.5.4l.7 1.5c.2.5 0 1-.4 1.3l-.6.4c.5 1.2 1.4 2.1 2.6 2.7l.4-.6c.3-.4.9-.6 1.3-.4l1.5.7c.6.3.8.9.4 1.5l-.6.8c-.5.6-1.3.8-2 .5-2.8-1.1-4.6-3-5.7-5.7-.3-.7-.1-1.5.5-2z" fill="var(--card-blue)"/>
          </svg>
          <span>415-362-9184</span>
        </li>
        <li class="contact__item">
          <svg class="contact__icon" viewBox="0 0 22 22" aria-hidden="true">
            <circle cx="11" cy="11" r="10" fill="#ffffff"/>
            <rect x="5.5" y="7" width="11" height="8" rx="1" fill="none" stroke="var(--card-blue)" stroke-width="1.5"/>
            <path d="M5.8 7.5 11 11.5l5.2-4" fill="none" stroke="var(--card-blue)" stroke-width="1.5"/>
          </svg>
          <span>marisol.varnaccio@plumpost.example</span>
        </li>
      </ul>
    </section>

    <p class="notary">Notary Public Serving Sonoma County</p>
  </article>
</main>
</body>
</html>
```